Life Coaching and Career Coaching company needs new website with bold, modern, videos

We need a whole new website that is heavy on video. We are a small company who sells personal wellbeing services like career coaching, life coaching, and group coaching programs. The programs all help people design a better life.
FULL BRIEF ATTACHED and STYLE GUIDE
Also, look at https://www.pinevaultery.com/coaching and corvanly.com and https://www.tarnwick.life/ for a small amount of inspiration.

Industry/Entity Type

personal well-being/life coaching/career coaching

Number of Pages Required

3 page

Other font styles liked:
• fonts are in the brief

Requirements
Must have
• read the brief please - it's all in there. (things like the look, feel, how it will have lots of video, etc,)
Nice to have
• something really different looking and breakthrough. visually stunning. very trustworthy. Please read the brief, its all in there.
Should not have
• should not look like other life coaching websites. must have video!

```html
<!DOCTYPE html>
<html lang="en">
<head>
<meta charset="utf-8">
<title>Brightpath Studio — Coaching</title>
<link href="https://fonts.googleapis.com/css2?family=Playfair+Display:wght@600;700&family=Poppins:wght@400;500;600&display=swap" rel="stylesheet">
<style>
:root{
  --teal:#0b5a5c;
  --teal-deep:#015659;
  --ink:#1d1d1d;
  --muted:#4a4a4a;
  --blush:#fdf1f0;
  --coral:#e8584f;
  --charcoal:#2f2f2f;
  --field:#f3f3f3;
  --white:#ffffff;
  --grey-btn:#a9a9a9;
}
*{margin:0;padding:0;box-sizing:border-box}
html,body{width:1200px;height:4717px;overflow:hidden}
body{position:relative;font-family:'Poppins',sans-serif;color:var(--ink);background:var(--white)}
.abs{position:absolute}
.serif{font-family:'Playfair Display',serif;font-weight:700}
.accent{color:var(--teal)}
.hot{color:var(--coral)}
.btn{position:absolute;display:flex;align-items:center;justify-content:center;gap:6px;border-radius:30px;font-size:13px;font-weight:600}
.btn-teal{background:var(--teal);color:var(--white)}
.btn-white{background:var(--white);color:var(--teal)}
.media{position:absolute;overflow:hidden}
.play{position:absolute;width:0;height:0;border-top:24px solid transparent;border-bottom:24px solid transparent;border-left:40px solid var(--coral)}
.label{font-size:14px;color:var(--teal);text-align:center}
.center-text{left:0;width:1200px;text-align:center}

/* nav */
.hero-tint{left:432px;top:0;width:768px;height:491px;background:var(--blush)}
.nav-line{left:0;top:94px;width:1200px;height:1px;background:#e6e6e6}
.brand{font-size:22px;font-weight:500;color:#555;letter-spacing:1px}
.nav-links{left:400px;top:40px;display:flex;gap:27px;font-size:13px;color:#555}
.nav-links .active{color:var(--ink);border-bottom:2px solid var(--teal);padding-bottom:4px}

/* hero */
.hero-title{left:117px;top:146px;font-size:51px;line-height:67px;width:760px}
.hero-copy{left:117px;top:306px;width:365px;font-size:14px;line-height:22.5px;color:#333}
.video-caption{left:24px;bottom:24px;color:var(--white);font-size:15px}

/* about */
.section-title{font-size:36px;line-height:51px}
.quote{font-size:13.5px;color:#555;line-height:21px}
.body-copy{font-size:14px;line-height:22px;color:#333}

/* solutions */
.band-teal{left:0;top:1163px;width:1200px;height:918px;background:var(--teal-deep)}
.sol-label{left:117px;top:1247px;font-size:14px;color:var(--coral)}
.sol-title{left:117px;top:1273px;color:var(--white);font-size:36px;line-height:52px;width:640px}
.sol-copy{left:117px;top:1452px;width:640px;color:var(--white);font-size:14px;line-height:22px}
.card-caption{position:absolute;color:var(--white);font-size:16px;font-weight:600}
.dots{left:517px;top:1996px;width:168px;height:2px;background:rgba(255,255,255,.6)}
.dots span{position:absolute;left:30px;top:-2px;width:48px;height:6px;border-radius:3px;background:var(--white)}

/* testimonials */
.band-dark{left:0;top:2698px;width:1200px;height:801px;background:var(--charcoal)}
.quote-mark{left:48px;top:38px;font-family:'Playfair Display',serif;font-size:130px;line-height:1;color:var(--ink)}
.pill{position:absolute;top:3367px;width:216px;height:51px;border:2px solid var(--white);border-radius:30px;color:var(--white);display:flex;align-items:center;justify-content:center;font-size:15px;font-weight:500}
.pill-hot{background:var(--white);color:var(--coral)}

/* contact */
.contact-title{left:117px;top:3630px;width:400px;font-size:36px;line-height:52px}
.contact-list{left:117px;top:4042px;font-size:16px}
.contact-list li{list-style:none;display:flex;align-items:center;gap:28px;height:37px}
.form-card{left:647px;top:3613px;width:436px;height:615px;background:var(--white);box-shadow:0 10px 40px rgba(0,0,0,.12);border-radius:4px}
.field{position:absolute;left:51px;background:var(--field);border-radius:3px;font-size:12px;color:#9a9a9a;padding:14px 12px}

/* footer */
.footer{left:0;top:4303px;width:1200px;height:414px;background:var(--teal-deep);color:var(--white)}
.foot-col{position:absolute;top:92px;font-size:13px}
.foot-col h4{font-size:13.5px;font-weight:600;margin-bottom:14px}
.foot-col li{list-style:none;height:33px}
</style>
</head>
<body>

<!-- header -->
<div class="abs hero-tint"></div>
<div class="abs nav-line"></div>
<div class="abs brand" style="left:117px;top:30px">BRIGHTPATH STUDIO</div>
<nav class="abs nav-links">
  <span class="active">Home</span><span>About us</span><span>Solutions</span><span>Resources ⌄</span><span>Testimonials</span><span>Blogs</span>
</nav>
<a class="btn btn-teal" style="left:947px;top:27px;width:136px;height:44px">Get Started</a>

<!-- hero -->
<h1 class="abs serif hero-title">Unleash Your <span class="accent">Potential</span>, Unleash Your <span class="accent">Power</span>.</h1>
<p class="abs hero-copy">Unlock your potential with personalized coaching services tailored to your unique journey. At Brightpath Studio, we are dedicated to helping you design the life you deserve through transformative programs that foster personal growth and empowerment. Embrace change, thrive, and cultivate holistic well-being</p>
<a class="btn btn-teal" style="left:117px;top:489px;width:150px;height:43px">Get Started ↗</a>
<a class="btn" style="left:282px;top:489px;width:150px;height:43px;background:var(--grey-btn);color:var(--white)">Watch Demo ↗</a>
<div class="media" role="img" aria-label="Video still of two women talking across a table in a bright office" style="left:526px;top:234px;width:557px;height:352px;border-radius:18px;background:linear-gradient(135deg,#2aa9a9,#137878 60%,#0d4f52)">
  <div class="play" style="left:262px;top:150px"></div>
  <div class="abs video-caption">Watch project demo (04:21)</div>
</div>

<!-- about -->
<div class="abs label center-text" style="top:703px">About Brightpath Studio</div>
<h2 class="abs serif section-title center-text" style="top:731px;color:#2b2b2b;font-weight:600">Our Journey of Empowerment:<br>Unveiling the Heart and Soul Behind<br>Our Holistic <span class="accent">Well-being</span> Mission.</h2>
<p class="abs quote center-text" style="top:911px">"SUCCESS IS NOT FINAL, FAILURE IS NOT FATAL: IT IS THE COURAGE<br>TO CONTINUE THAT COUNTS."</p>
<p class="abs body-copy center-text" style="top:974px">Driven by the belief that everyone deserves to lead a purposeful<br>life, we are on a mission to ignite positive transformations. Our<br>commitment to nurturing personal growth and well-being is at<br>the heart of everything we do.</p>

<!-- solutions -->
<div class="abs band-teal"></div>
<div class="abs sol-label">Discover Our Solutions</div>
<h2 class="abs serif sol-title" style="font-weight:600">Discover Tailored and Innovative Solutions Crafted Just for You by Our Expert Team.</h2>
<a class="btn btn-white" style="left:947px;top:1328px;width:136px;height:44px">Get Started</a>
<p class="abs sol-copy">Our expert team is dedicated to crafting tailored and innovative solutions designed to elevate your success. We strive to transcend the ordinary and make a tangible impact, ensuring that you receive nothing short of exceptional results. Explore our array of services and unlock the potential for transformative growth and success.</p>

<div class="media" role="img" aria-label="Person standing on a mountain top under a cloudy sky" style="left:0;top:1618px;width:288px;height:317px;border-radius:0 14px 14px 0;background:linear-gradient(180deg,#8aa0b6,#4c6a86 60%,#2c3f52)">
  <svg class="abs" style="left:112px;top:140px" width="52" height="36" viewBox="0 0 52 36"><path d="M50 18H4M20 2L4 18l16 16" fill="none" stroke="#fff" stroke-width="3"/></svg>
</div>
<div class="media" role="img" aria-label="Video still of two women in a career coaching session before a brick wall" style="left:308px;top:1601px;width:584px;height:350px;border-radius:14px;background:linear-gradient(180deg,#c9987e,#a86d55 50%,#4a3a36)">
  <div class="abs" style="right:40px;top:26px;color:var(--white);font-size:15px">Watch video (02:51)</div>
  <div class="play" style="left:274px;top:151px"></div>
  <div class="card-caption" style="left:38px;bottom:22px">career coaching</div>
  <div class="abs" style="right:38px;bottom:24px;color:var(--white);font-size:12px">See more →</div>
</div>
<div class="media" role="img" aria-label="Woman working in a modern studio with neon sign" style="left:912px;top:1618px;width:288px;height:317px;border-radius:14px 0 0 14px;background:linear-gradient(135deg,#9aa4a8,#5f6b70 60%,#3a3f42)">
  <svg class="abs" style="left:122px;top:140px" width="52" height="36" viewBox="0 0 52 36"><path d="M2 18h46M32 2l16 16-16 16" fill="none" stroke="#fff" stroke-width="3"/></svg>
</div>
<div class="abs dots"><span></span></div>

<!-- testimonials -->
<div class="abs label center-text" style="top:2240px">Discover Our Solutions</div>
<h2 class="abs serif section-title center-text" style="top:2265px;color:#2b2b2b;font-weight:600">Voices of Success: Real Stories, <span class="accent">Real<br>Impact</span> – Hear Directly from Our<br>Satisfied Clients.</h2>
<p class="abs quote center-text" style="top:2450px">"THE ONLY LIMIT TO OUR REALIZATION OF TOMORROW WILL BE OUR DOUBTS OF<br>TODAY."</p>
<p class="abs body-copy center-text" style="top:2513px">Hear firsthand how our tailored solutions have transformed their businesses and<br>unlocked new levels of success.</p>

<div class="abs band-dark"></div>
<div class="media" role="img" aria-label="Portrait of a bearded client in teal tone" style="left:66px;top:2614px;width:146px;height:352px;border-radius:12px;background:linear-gradient(180deg,#2c8f8c,#15514f)">
  <svg class="abs" style="left:46px;top:158px" width="52" height="36" viewBox="0 0 52 36"><path d="M50 18H4M20 2L4 18l16 16" fill="none" stroke="#fff" stroke-width="3"/></svg>
</div>
<div class="media" role="img" aria-label="Video testimonial from a smiling client with glasses" style="left:227px;top:2614px;width:585px;height:352px;border-radius:12px;background:linear-gradient(90deg,#e4e5e6,#d6d7d9 55%,#c6c8ca)">
  <div class="abs quote-mark">”</div>
  <div class="play" style="left:265px;top:150px"></div>
  <div class="abs" style="left:24px;bottom:34px;font-size:15px;color:#333">Watch testimonial (02:51)</div>
</div>
<div class="media" role="img" aria-label="Portrait of a client outdoors in green tone" style="left:826px;top:2614px;width:147px;height:352px;border-radius:12px;background:linear-gradient(180deg,#4aa06a,#1f5a3c)"></div>
<div class="media" role="img" aria-label="Portrait of a smiling client in teal tone" style="left:987px;top:2614px;width:147px;height:352px;border-radius:12px;background:linear-gradient(180deg,#3aa7a4,#1a5c5a)">
  <svg class="abs" style="left:50px;top:158px" width="52" height="36" viewBox="0 0 52 36"><path d="M2 18h46M32 2l16 16-16 16" fill="none" stroke="#fff" stroke-width="3"/></svg>
</div>
<div class="media" role="img" aria-label="Portrait of a client in teal tone" style="left:1149px;top:2614px;width:60px;height:352px;border-radius:12px 0 0 12px;background:linear-gradient(180deg,#36a09c,#1a5856)"></div>

<h2 class="abs serif section-title center-text" style="top:3080px;color:var(--white);font-weight:600">Elevating Success: Embracing Creativity<br>to Breathe Life into <span class="hot">Dreams</span> and<br>Transform Visions into <span class="hot">Reality.</span></h2>
<p class="abs body-copy center-text" style="top:3252px;color:var(--white)">Our coaching website is your gateway to unlocking potential, realizing<br>dreams, and achieving unparalleled success. Embrace creativity, redefine<br>success, and elevate your life today.</p>
<div class="pill" style="left:233px">LIFE COACHING</div>
<div class="pill" style="left:491px">CAREER COACHING</div>
<div class="pill pill-hot" style="left:749px">GROUP COACHING</div>

<!-- contact -->
<div class="abs" style="left:117px;top:3601px;font-size:14px;color:var(--teal)">Contact Us</div>
<h2 class="abs serif contact-title" style="color:#2b2b2b;font-weight:600">Joining Hands: Building Relationships, and Enriching Lives – Reach Out to Us Today.</h2>
<p class="abs body-copy" style="left:117px;top:3855px;width:470px;font-size:14px;line-height:22.5px">We welcome the opportunity to engage with you. Whether you have questions, innovative ideas to share, or simply wish to extend a friendly greeting, our doors are open, and our ears are ready to listen. Feel free to reach out to us via a message, a phone call, or by visiting us in person. We eagerly anticipate the chance to connect with you.</p>
<ul class="abs contact-list">
  <li><svg width="16" height="12" viewBox="0 0 16 12"><rect width="16" height="12" rx="1" fill="#0b5a5c"/><path d="M1 1l7 6 7-6" fill="none" stroke="#fff" stroke-width="1.4"/></svg>hello@brightpathstudio.com</li>
  <li><svg width="16" height="16" viewBox="0 0 24 24"><path d="M6.6 10.8a15 15 0 006.6 6.6l2.2-2.2a1 1 0 011-.25 11.4 11.4 0 003.6.57 1 1 0 011 1V20a1 1 0 01-1 1A17 17 0 013 4a1 1 0 011-1h3.5a1 1 0 011 1 11.4 11.4 0 00.57 3.6 1 1 0 01-.25 1z" fill="#0b5a5c"/></svg>00 318 462 5071</li>
  <li><svg width="16" height="16" viewBox="0 0 16 16"><circle cx="8" cy="8" r="6.5" fill="none" stroke="#0b5a5c" stroke-width="1.6"/><circle cx="8" cy="8" r="2.6" fill="#0b5a5c"/></svg>4187 Harlow Crest, West Amberly, NE</li>
</ul>

<div class="abs form-card">
  <div class="abs" style="left:51px;top:46px;font-size:22px;font-weight:500">Let's get in touch</div>
  <div class="abs btn-teal" style="left:51px;top:102px;width:333px;height:46px;border-radius:3px;display:flex;align-items:center;justify-content:center;font-size:14px;font-weight:500">Get started now</div>
  <div class="abs" style="left:51px;top:185px;width:333px;height:1px;background:#dcdcdc"></div>
  <div class="abs" style="left:202px;top:178px;padding:0 8px;background:var(--white);font-size:9px;color:#999">OR</div>
  <div class="field" style="top:210px;width:158px;height:46px">First Name</div>
  <div class="field" style="left:226px;top:210px;width:158px;height:46px">Last Name</div>
  <div class="field" style="top:269px;width:333px;height:44px">Email Adress</div>
  <div class="field" style="top:327px;width:333px;height:45px">Phone Number</div>
  <div class="field" style="top:386px;width:333px;height:119px">Tell us how we can help you</div>
  <div class="abs btn-teal" style="left:51px;top:527px;width:121px;height:46px;border-radius:3px;display:flex;align-items:center;justify-content:center;font-size:14px;font-weight:500">Send</div>
</div>

<!-- footer -->
<footer class="abs footer">
  <div class="abs" style="left:117px;top:92px;font-size:34px;font-weight:500;letter-spacing:1px">BRIGHTPATH</div>
  <p class="abs" style="left:117px;top:157px;width:230px;font-size:12.5px;line-height:20px">Our passion drives us to create meaningful experiences and exceed expectations every step of the way.</p>
  <div class="foot-col" style="left:434px"><h4>DISCOVER</h4><ul><li>Our Project</li><li>About Us</li><li>Solutions</li><li>Testimonials</li><li>Our Team</li></ul></div>
  <div class="foot-col" style="left:586px"><h4>CONTACT</h4><ul><li>Contact Us</li><li>FAQs</li><li>Privacy Policy</li><li>Terms of Service</li></ul></div>
  <div class="foot-col" style="left:762px"><h4>RESOURCES</h4><ul><li>Blog</li><li>Partners</li><li>Careers</li><li>Customer Support</li></ul></div>
  <div class="foot-col" style="left:953px"><h4>FOLLOW US</h4><ul><li>Photo Feed</li><li>Microblog</li><li>Community Page</li><li>Work Network</li></ul></div>
  <div class="abs" style="left:58px;top:332px;width:1084px;height:1px;background:rgba(255,255,255,.25)"></div>
  <div class="abs" style="right:117px;top:362px;font-size:12.5px">© 2023 Brightpath Studio. All rights reserved.</div>
</footer>

</body>
</html>
```